Tri-fold Brochure Design for Banking Business

The brochure we have needs to be improved - more business like and more attractive. Logo file and brochure is attached. I would like to be able to edit the text after you get done. Your ideas and changes to text are welcome. See our website www.korvanbridgegrp.com for our theme. We can use indesign to edit the text after you complete. However, please make changes to the text we have in the design that it uploaded. Your comments and changes are welcome.

Target Market(s)

Human Resources and learning & development staff at the global investment banks - Pellham Trask, QWNR, etc.

Industry/Entity Type

Investment Banking

Logo Text

Korvan Bridge Group

Font styles to use
Serif
Sans Serif

Colors
33a6d7
0493ce
3277b5
fbf289
fdf9cf
fbee3e
0555a3
85acd3

Requirements
Must have
• Must be similar to our website www.korvanbridgegrp.com. Needs to be business-like, clean fonts, sharp design. Our logo - of course.
Nice to have
• City images - seems to be our theme.

```html
<!DOCTYPE html>
<html lang="en">
<head>
<meta charset="utf-8">
<title>Korvan Bridge Group – Tri-fold Brochure</title>
<link rel="stylesheet" href="https://fonts.googleapis.com/css2?family=Oswald:wght@300;400;600;700&family=Montserrat:wght@400;500;600;700&display=swap">
<style>
  :root{
    --blue:#0a4b9c;
    --blue-deep:#073c82;
    --blue-bright:#0555a3;
    --yellow:#f7e21c;
    --yellow-soft:#fbf289;
    --sky-top:#cfe6f6;
    --sky-bottom:#5f93c2;
    --paper:#f3f4f6;
    --grey-text:#555a60;
    --grey-light:#9aa0a6;
    --map-grey:#b9bcc0;
    --ink:#111418;
    --page-bg:#dcdcdd;
  }
  *{box-sizing:border-box;margin:0;padding:0}
  html,body{width:1200px;height:800px;overflow:hidden;background:var(--page-bg)}
  .spread{position:absolute;left:45px;top:30px;width:1110px;height:740px;display:flex;box-shadow:0 6px 24px rgba(0,0,0,.18)}
  .panel{position:relative;width:370px;height:740px;overflow:hidden}
  .panel svg.bg{position:absolute;inset:0}
  .top-band{position:absolute;left:0;top:0;width:100%;height:14px;background:var(--blue)}
  .top-band::after{content:"";position:absolute;top:0;width:46px;height:14px;background:var(--yellow)}
  .flap .top-band::after{left:40px}
  .cover .top-band::after{right:20px}
  .contact .top-band::after{display:none}

  /* flap panel */
  .flap-copy{position:absolute;left:40px;top:440px;width:270px;font:500 12.5px/1.5 "Montserrat",sans-serif;color:var(--ink)}
  .flap-copy p{margin-bottom:16px}
  .flap-url{position:absolute;left:40px;bottom:78px;background:var(--ink);color:var(--yellow);font:600 12px/1 "Oswald",sans-serif;letter-spacing:.5px;padding:6px 10px}

  /* contact panel */
  .contact{background:var(--paper)}
  .contact-title{position:absolute;left:0;width:100%;top:60px;text-align:center;font:300 34px/1 "Oswald",sans-serif;color:var(--grey-text);text-transform:uppercase}
  .contact-title strong{font-weight:700;color:var(--blue)}
  .mail-icon{position:absolute;left:160px;top:112px}
  .regions{position:absolute;left:0;width:100%;top:170px;text-align:center;font-family:"Montserrat",sans-serif}
  .region-name{font-weight:700;font-size:12px;color:var(--blue);text-transform:uppercase;letter-spacing:.3px}
  .region-mail{font-size:12px;color:var(--ink);margin-bottom:6px}
  .world-map{position:absolute;left:40px;top:360px}
  .worldwide{position:absolute;left:40px;top:472px;font:700 15px/1 "Montserrat",sans-serif;color:var(--blue);text-transform:uppercase}
  .worldwide span{display:block;font-weight:600;font-size:10px;color:var(--grey-text);margin-top:3px;letter-spacing:.5px}
  .globe-icon{position:absolute;left:158px;top:590px}
  .contact-url{position:absolute;left:0;width:100%;top:655px;text-align:center;font:500 19px/1 "Oswald",sans-serif;color:var(--yellow);letter-spacing:.5px}

  /* cover panel */
  .brand{position:absolute;left:50px;top:52px;display:flex;align-items:center;gap:12px}
  .brand-mark{width:30px;height:30px;background:var(--blue)}
  .brand-name{font:600 22px/1.05 "Oswald",sans-serif;color:var(--ink);text-transform:uppercase;letter-spacing:1px}
  .tagline{position:absolute;left:0;width:100%;top:598px;text-align:center;font-family:"Oswald",sans-serif;text-transform:uppercase}
  .tagline-light{font-weight:300;font-size:24px;color:#fff;letter-spacing:.3px}
  .tagline-bold{font-weight:700;font-size:33px;color:var(--yellow);line-height:1.05}
  .cover-url{display:inline-block;margin-top:10px;background:var(--yellow);color:var(--blue-deep);font:600 12.5px/1 "Oswald",sans-serif;padding:6px 14px;letter-spacing:.5px}
  .stitch{position:absolute;left:0;bottom:22px;width:100%;border-top:2px dashed rgba(255,255,255,.35)}
</style>
</head>
<body>
<main class="spread">

  <!-- Inner flap -->
  <section class="panel flap">
    <svg class="bg" width="370" height="740" viewBox="0 0 370 740">
      <defs>
        <linearGradient id="harbourSky" x1="0" y1="0" x2="0" y2="1">
          <stop offset="0" stop-color="#6cc0e6"/><stop offset=".6" stop-color="#8a96a4"/><stop offset="1" stop-color="#3f6f98"/>
        </linearGradient>
      </defs>
      <rect width="370" height="740" fill="#ffffff"/>
      <rect width="370" height="380" fill="url(#harbourSky)" role="img" aria-label="Photo of a city skyline across a harbour"/>
      <circle cx="20" cy="250" r="72" fill="#7e97ad" stroke="#fff" stroke-width="6" role="img" aria-label="Round photo inset of a waterfront"/>
      <polygon points="0,380 370,300 370,740 0,740" fill="#ffffff"/>
      <polygon points="0,420 250,360 370,330 370,390 140,740 0,740" fill="var(--yellow)"/>
      <polygon points="190,360 370,300 370,330 240,380" fill="#dce6ef" opacity=".8"/>
      <polygon points="0,680 370,650 370,740 0,740" fill="var(--blue)"/>
    </svg>
    <div class="top-band"></div>
    <div class="flap-copy">
      <p>Our global team efficiently provides training and logistical support, whatever the location.</p>
      <p>We have extensive networks of professionals and assessors.</p>
      <p>Our programs complement the work of HR teams, fast and efficient.</p>
    </div>
    <div class="flap-url">WWW.KORVANBRIDGEGRP.COM</div>
  </section>

  <!-- Contact panel -->
  <section class="panel contact">
    <svg class="bg" width="370" height="740" viewBox="0 0 370 740">
      <polygon points="0,590 230,545 370,520 370,555 230,580 0,620" fill="var(--yellow)"/>
      <polygon points="0,620 230,580 370,555 370,740 0,740" fill="var(--blue)"/>
      <line x1="0" y1="718" x2="370" y2="718" stroke="rgba(255,255,255,.35)" stroke-width="2" stroke-dasharray="4 3"/>
    </svg>
    <div class="top-band"></div>
    <h2 class="contact-title">Get in <strong>Touch</strong></h2>
    <svg class="mail-icon" width="50" height="50" viewBox="0 0 50 50" aria-hidden="true">
      <circle cx="25" cy="25" r="22" fill="#fff" stroke="var(--blue)" stroke-width="2"/>
      <rect x="14" y="18" width="22" height="15" fill="none" stroke="var(--blue)" stroke-width="2"/>
      <polyline points="14,18 25,27 36,18" fill="none" stroke="var(--blue)" stroke-width="2"/>
    </svg>
    <div class="regions">
      <div class="region-name">Global</div>
      <div class="region-mail">nadia.ferrante@korvanbridgegrp.com</div>
      <div class="region-name">Asia</div>
      <div class="region-mail">owen.pratt@korvanbridgegrp.com</div>
      <div class="region-name">United States</div>
      <div class="region-mail">paul.renner@korvanbridgegrp.com</div>
      <div class="region-name">Europe</div>
      <div class="region-mail">lena.hardy@korvanbridgegrp.com</div>
    </div>
    <svg class="world-map" width="290" height="110" viewBox="0 0 290 110" role="img" aria-label="World map">
      <rect width="290" height="110" rx="8" fill="var(--map-grey)" opacity=".7"/>
    </svg>
    <div class="worldwide">Worldwide<span>Training Service</span></div>
    <svg class="globe-icon" width="54" height="54" viewBox="0 0 54 54" aria-hidden="true">
      <circle cx="27" cy="27" r="24" fill="none" stroke="var(--yellow)" stroke-width="2.5"/>
      <circle cx="27" cy="27" r="13" fill="none" stroke="#fff" stroke-width="2"/>
      <ellipse cx="27" cy="27" rx="6" ry="13" fill="none" stroke="#fff" stroke-width="2"/>
      <line x1="14" y1="27" x2="40" y2="27" stroke="#fff" stroke-width="2"/>
    </svg>
    <div class="contact-url">WWW.KORVANBRIDGEGRP.COM</div>
  </section>

  <!-- Cover panel -->
  <section class="panel cover">
    <svg class="bg" width="370" height="740" viewBox="0 0 370 740">
      <defs>
        <linearGradient id="coverSky" x1="0" y1="0" x2="0" y2="1">
          <stop offset="0" stop-color="var(--sky-top)"/><stop offset=".55" stop-color="#8fb4d4"/><stop offset="1" stop-color="var(--sky-bottom)"/>
        </linearGradient>
      </defs>
      <rect width="370" height="740" fill="#eaf3fa"/>
      <rect y="130" width="370" height="440" fill="url(#coverSky)" role="img" aria-label="Photo of a city skyline with a tall tower by the water"/>
      <rect width="370" height="140" fill="#e6f1f9" opacity=".9"/>
      <polygon points="0,420 0,470 230,600 280,590" fill="var(--yellow)"/>
      <polygon points="0,470 230,600 370,520 370,740 0,740" fill="var(--blue)"/>
      <polygon points="230,600 370,430 370,520" fill="#ffffff" opacity=".35"/>
      <polygon points="330,560 370,540 370,590" fill="var(--yellow)"/>
    </svg>
    <div class="top-band"></div>
    <div class="brand">
      <span class="brand-mark"></span>
      <span class="brand-name">Korvan Bridge Group</span>
    </div>
    <div class="tagline">
      <div class="tagline-light">Your Expert Training and</div>
      <div class="tagline-bold">Consulting Partner</div>
      <div class="cover-url">WWW.KORVANBRIDGEGRP.COM</div>
    </div>
    <div class="stitch"></div>
  </section>

</main>
</body>
</html>
```